DEAN COLLOPY PROPERTY SERVICES

I want a business card that is clean and simple.
'Dean Collopy Property Services' is the title.
Somewhere on the card needs to be 'Carpentry, Tiling, painting and garden services'

On the back of card
PH 087 394 1526
email: deancollopypropertyservices@fernmail.net

I have attached a picture of my other business. I would like the font and design to be similar to the bathroom business.

Many thanks.

```html
<!DOCTYPE html>
<html lang="en">
<head>
<meta charset="utf-8">
<title>Dean Collopy Property Services – Business Card</title>
<link rel="stylesheet" href="https://fonts.googleapis.com/css2?family=Montserrat:wght@600&family=Roboto:wght@400;500&family=Exo+2:ital,wght@0,600;1,400&display=swap">
<style>
  :root {
    --page: #2b2b2b;
    --card: #232323;
    --card-front: #242424;
    --ink-gloss: #0e0e0e;
    --band: #35383b;
    --band-dark: #2a2c2e;
    --white: #ffffff;
    --soft: #e6e6e6;
  }
  * { box-sizing: border-box; margin: 0; padding: 0; }
  html, body {
    width: 1200px; height: 1138px; overflow: hidden;
    background: var(--page);
  }
  .canvas { position: relative; width: 1200px; height: 1138px; }

  .card {
    position: absolute; left: 276px; width: 620px; height: 375px;
    border-radius: 14px; overflow: hidden; background: var(--card);
  }
  .card--front { top: 186px; background: var(--card-front); }
  .card--back { top: 608px; }

  /* Front */
  .front-brand {
    position: absolute; left: 0; right: 0; top: 146px; text-align: center;
    color: var(--ink-gloss); font-family: "Montserrat", sans-serif; font-weight: 600;
  }
  .front-brand .brand-name { font-size: 58px; line-height: 1; letter-spacing: -0.5px; }
  .front-brand .brand-sub { font-size: 19px; letter-spacing: 8px; margin-top: 6px; }
  .front-services {
    position: absolute; left: 0; right: 0; top: 262px; text-align: center;
    font-family: "Roboto", sans-serif; font-size: 17px; color: var(--ink-gloss);
  }

  /* Back */
  .back-brand {
    position: absolute; right: 40px; top: 72px; text-align: right;
    color: var(--white); font-family: "Montserrat", sans-serif; font-weight: 600;
  }
  .back-brand .brand-name { font-size: 44px; line-height: 1; letter-spacing: -0.3px; }
  .back-brand .brand-sub { font-size: 15px; letter-spacing: 5.5px; margin-top: 5px; }

  .holder {
    position: absolute; left: 44px; top: 206px; display: flex; align-items: baseline; gap: 12px;
    color: var(--white);
  }
  .holder .name { font-family: "Exo 2", sans-serif; font-weight: 600; font-size: 24px; }
  .holder .role { font-family: "Exo 2", sans-serif; font-style: italic; font-size: 14px; color: var(--soft); }

  .contact-band {
    position: absolute; left: 0; right: 0; top: 244px; bottom: 0;
    background: linear-gradient(180deg, var(--band), var(--band-dark));
  }
  .contact-list {
    position: absolute; left: 44px; top: 26px; list-style: none;
    font-family: "Roboto", sans-serif; font-size: 16px; color: var(--soft);
  }
  .contact-list li { display: flex; align-items: center; gap: 9px; height: 24px; }
  .contact-list svg { width: 18px; height: 18px; flex: none; }
  .back-services {
    position: absolute; left: 44px; top: 86px;
    font-family: "Roboto", sans-serif; font-size: 16px; color: var(--soft);
  }
</style>
</head>
<body>
<div class="canvas">

  <section class="card card--front" aria-label="Card front">
    <div class="front-brand">
      <div class="brand-name">Dean Collopy</div>
      <div class="brand-sub">PROPERTY SERVICES</div>
    </div>
    <p class="front-services">Carpentry &nbsp;|&nbsp; Tiling &nbsp;|&nbsp; Painting &nbsp;|&nbsp; Garden Services</p>
  </section>

  <section class="card card--back" aria-label="Card back">
    <div class="back-brand">
      <div class="brand-name">Dean Collopy</div>
      <div class="brand-sub">PROPERTY SERVICES</div>
    </div>

    <div class="holder">
      <span class="name">Dean Collopy</span>
      <span class="role">Owner &amp; Director</span>
    </div>

    <div class="contact-band">
      <ul class="contact-list">
        <li>
          <svg viewBox="0 0 20 20" aria-hidden="true">
            <circle cx="10" cy="10" r="9" fill="none" stroke="#e6e6e6" stroke-width="1.3"/>
            <path d="M7 5.5l1.6 2.2-1 1.1a6 6 0 0 0 3.6 3.6l1.1-1 2.2 1.6-1 1.6c-3.8 0-7.1-3.3-7.1-7.1z" fill="#e6e6e6"/>
          </svg>
          087 394 1526
        </li>
        <li>
          <svg viewBox="0 0 20 20" aria-hidden="true">
            <circle cx="10" cy="10" r="9" fill="none" stroke="#e6e6e6" stroke-width="1.3"/>
            <rect x="5.2" y="6.8" width="9.6" height="6.6" rx="0.8" fill="#e6e6e6"/>
            <path d="M5.6 7.3l4.4 3.4 4.4-3.4" fill="none" stroke="#35383b" stroke-width="1"/>
          </svg>
          deancollopypropertyservices@fernmail.net
        </li>
      </ul>
      <p class="back-services">Carpentry &nbsp;|&nbsp; Tiling &nbsp;|&nbsp; Painting &nbsp;|&nbsp; Garden Services</p>
    </div>
  </section>

</div>
</body>
</html>
```